Calloway Teaching Placements Business Cards

We need business cards designed for our growing recruitment business.
We have just launched our offices in Sydney Melbourne and have a well established business in Perth. We are a fun young firm that specialise in Early Years Education Recruitment.
Our vision mission values are below
Our Vision:
To be:
the single, nationally recognised leader in the Early Childhood Sector.
a multifaceted organisation with a network of expertly driven facilities in the Early Childhood Sector, acknowledged as an organisation of integrity, innovation, heart and community.

Our Mission:
To provide superior quality recruitment services and solutions to the Early Childhood sector.
We empower our candidates to succeed.
We engage in trusted partnerships with our clients.
We grow our business/network/community, with passion and integrity.

Our Values:

We… are REAL
think: CUSTOMER
find: SOLUTIONS
achieve: RESULTS
enjoy: WHAT WE DO

Our website is www.callowayteaching.com feel free to visit it for inspiration.
Name Felix Harrowby
Title National Director
1300 047 815
0412 736 205
felix@callowayplacements.com
website www.callowayteaching.com

I have attached our current business cards and logo designs to view

Target Market(s)

Recruitment

Industry/Entity Type

Business

Contact Information for Business Card

Name Felix Harrowby
Title National Director
1300 047 815
0412 736 205

Font styles to use
Serif

Requirements
Must have
• Company Values and the cities we have offices in Perth | Sydney | Melbourne
Nice to have
• Our Vision on the card
• Our Vision:
• To be a nationally recognised leader in the Early Childhood Sector.
• A multifaceted organisation with a network of expertly driven facilities in the Early Childhood Sector, acknowledged as an organisation of integrity, innovation, heart and community.

```html
<!DOCTYPE html>
<html lang="en">
<head>
<meta charset="utf-8">
<title>Calloway Teaching Placements – Business Cards</title>
<link rel="stylesheet" href="https://fonts.googleapis.com/css2?family=Montserrat:wght@400;500;600;700&display=swap">
<style>
  :root {
    --stage: #1d1f23;
    --navy-deep: #0c2c4f;
    --navy: #134a7c;
    --blue-glow: #2a8fd6;
    --sky: #29a3e0;
    --sky-soft: #5cc0f2;
    --ink: #0e2f52;
    --white: #ffffff;
    --paper: #ffffff;
  }
  * { box-sizing: border-box; margin: 0; padding: 0; }
  html, body { width: 1200px; height: 900px; overflow: hidden; }
  body {
    background: var(--stage);
    font-family: "Montserrat", Arial, sans-serif;
    position: relative;
  }
  .card {
    position: absolute;
    width: 640px;
    height: 366px;
    border-radius: 22px;
    overflow: hidden;
    box-shadow: 0 14px 40px rgba(0,0,0,.55);
  }

  /* ---------- Front: values card ---------- */
  .card-front {
    left: 80px; top: 56px;
    background:
      radial-gradient(circle at 50% 30%, rgba(60,160,230,.75) 0%, rgba(30,110,180,.35) 28%, rgba(0,0,0,0) 55%),
      linear-gradient(160deg, var(--navy) 0%, var(--navy-deep) 100%);
    color: var(--white);
    text-align: center;
  }
  .brand-row {
    position: absolute;
    top: 46px; left: 0; right: 0;
    display: flex; align-items: center; justify-content: center; gap: 16px;
  }
  .brand-mark {
    width: 62px; height: 62px;
    border: 3px solid var(--white);
    border-radius: 50%;
  }
  .brand-name {
    font-size: 33px; font-weight: 600; letter-spacing: 2px;
    color: var(--white);
  }
  .tagline {
    position: absolute; top: 124px; left: 0; right: 0;
    font-size: 14px; font-weight: 500; letter-spacing: .3px;
  }
  .band {
    position: absolute; left: 0; right: 0; height: 3px;
    background: linear-gradient(90deg, rgba(92,192,242,0) 0%, rgba(92,192,242,.7) 50%, rgba(92,192,242,0) 100%);
  }
  .band-top { top: 114px; }
  .band-bottom { top: 240px; }
  .values-label {
    position: absolute; top: 156px; left: 0; right: 0;
    font-size: 13px; font-weight: 600; letter-spacing: 1px; color: #0d3a66;
  }
  .values {
    position: absolute; top: 176px; left: 0; right: 0;
    font-size: 14.5px; line-height: 1.5;
  }
  .values .dot { color: var(--sky-soft); padding: 0 4px; }
  .vision {
    position: absolute; top: 256px; left: 30px; right: 30px;
    font-size: 13.6px; line-height: 1.45; color: var(--sky);
    font-weight: 500;
  }

  /* ---------- Back: contact card ---------- */
  .card-back {
    left: 480px; top: 470px;
    background: var(--paper);
  }
  .monogram-field {
    position: absolute; left: -150px; top: 96px;
    width: 420px; height: 420px;
  }
  .corner-tab {
    position: absolute; right: 150px; top: 0;
    width: 10px; height: 28px; background: var(--navy);
  }
  .contact {
    position: absolute; right: 34px; top: 62px;
    text-align: right; color: var(--ink);
  }
  .contact-name {
    font-size: 30px; font-weight: 700; letter-spacing: 1px; color: var(--sky);
  }
  .contact-title { font-size: 16px; font-weight: 500; margin-top: 2px; }
  .contact-cities { font-size: 15px; color: var(--sky); margin-top: 6px; }
  .contact-line {
    display: flex; justify-content: flex-end; align-items: center; gap: 8px;
    font-size: 16px; font-weight: 500; margin-top: 4px;
  }
  .contact-line svg { width: 13px; height: 13px; flex: none; }
  .contact-web { margin-top: 18px; }
</style>
</head>
<body>

  <section class="card card-front">
    <div class="brand-row">
      <span class="brand-mark"></span>
      <span class="brand-name">CALLOWAY TEACHING</span>
    </div>
    <div class="band band-top"></div>
    <p class="tagline">Bringing quality to education recruitment</p>
    <p class="values-label">OUR VALUES:</p>
    <p class="values">
      We… are REAL<span class="dot">•</span>Think: CUSTOMER<span class="dot">•</span>Find: SOLUTIONS<br>
      Achieve: RESULTS<span class="dot">•</span>Enjoy: WHAT WE DO
    </p>
    <div class="band band-bottom"></div>
    <p class="vision">
      To be a nationally recognised leader in the Early Childhood Sector.
      A multifaceted organisation with a network of expertly driven facilities in
      the Early Childhood Sector, acknowledged as an organisation of integrity,
      innovation, heart and community.
    </p>
  </section>

  <section class="card card-back">
    <svg class="monogram-field" viewBox="0 0 420 420" role="img" aria-label="Large circular brand emblem area">
      <defs>
        <linearGradient id="ringFade" x1="0" y1="0" x2="1" y2="1">
          <stop offset="0" stop-color="#29a3e0"/>
          <stop offset="1" stop-color="#134a7c"/>
        </linearGradient>
      </defs>
      <circle cx="210" cy="210" r="196" fill="#eef7fd" stroke="url(#ringFade)" stroke-width="12"/>
    </svg>
    <div class="corner-tab"></div>
    <div class="contact">
      <p class="contact-name">FELIX HARROWBY</p>
      <p class="contact-title">National Director</p>
      <p class="contact-cities">Perth | Sydney | Melbourne</p>
      <p class="contact-line">1300 047 815
        <svg viewBox="0 0 24 24"><path fill="#29a3e0" d="M6.6 10.8a15 15 0 0 0 6.6 6.6l2.2-2.2a1 1 0 0 1 1-.25 11.4 11.4 0 0 0 3.6.57 1 1 0 0 1 1 1V20a1 1 0 0 1-1 1A17 17 0 0 1 3 4a1 1 0 0 1 1-1h3.5a1 1 0 0 1 1 1c0 1.25.2 2.45.57 3.57a1 1 0 0 1-.25 1z"/></svg>
      </p>
      <p class="contact-line">0412 736 205
        <svg viewBox="0 0 24 24"><rect x="6" y="2" width="12" height="20" rx="2" fill="none" stroke="#29a3e0" stroke-width="2.4"/><circle cx="12" cy="18" r="1.3" fill="#29a3e0"/></svg>
      </p>
      <p class="contact-line">felix@callowayplacements.com
        <svg viewBox="0 0 24 24"><rect x="2" y="5" width="20" height="14" rx="2" fill="none" stroke="#29a3e0" stroke-width="2.4"/><path d="M3 6l9 7 9-7" fill="none" stroke="#29a3e0" stroke-width="2.4"/></svg>
      </p>
      <p class="contact-line">www.callowayteaching.com
        <svg viewBox="0 0 24 24"><circle cx="12" cy="12" r="9.5" fill="none" stroke="#29a3e0" stroke-width="2.2"/><path d="M2.5 12h19M12 2.5c3 3 3 16 0 19M12 2.5c-3 3-3 16 0 19" fill="none" stroke="#29a3e0" stroke-width="1.8"/></svg>
      </p>
    </div>
  </section>

</body>
</html>
```